Award winning pet photographer needs business card and letterhead

Business card and letterhead for our Pet photography business. We specialize in studio portraits of dogs.

Target Market(s)

Wealthy and middle class dog owners who would like photos of their dogs as wall art.

Industry/Entity Type

Portrait Photography

Contact Information for Business Card

Our business name is Tails of Glee Pet Photography. Would be good to include dog and a heart, bright colours and a modern design

Font styles to use
Sans Serif

Colors
f04a50
f68d4d
faa54b
33a6d7
33b8a4
abd036

Requirements
Must have
• Business name: Tails of Glee Pet Photography
• Phone number: 0497 560314
• Email: declan@kwstudio.com.au
• Website:www.tailsofglee.com.au
• Photographer: Declan Farrow
Nice to have
• In Addition letterhead should include
• Studio address 27 Fennick Court, Elmvale 6112
• Postal Address 8 Ormsby Ave, West Elmvale 6112

```html
<!DOCTYPE html>
<html lang="en">
<head>
<meta charset="utf-8">
<title>Tails of Glee Pet Photography – Business Card</title>
<link rel="stylesheet" href="https://fonts.googleapis.com/css2?family=Arimo:wght@400;700&display=swap">
<style>
  :root {
    --backdrop: #4a4a4a;
    --card: #000000;
    --brand-red: #f04a50;
    --text-white: #ffffff;
    --font-main: "Arimo", Arial, sans-serif;
  }
  html, body {
    margin: 0;
    padding: 0;
    width: 999px;
    height: 1200px;
    overflow: hidden;
    background: var(--backdrop);
    font-family: var(--font-main);
  }
  .canvas {
    position: relative;
    width: 999px;
    height: 1200px;
  }
  .card {
    position: absolute;
    left: 34px;
    width: 931px;
    height: 532px;
    background: var(--card);
  }
  .card--front { top: 72px; }
  .card--back { top: 626px; }

  .brand {
    position: absolute;
    display: flex;
    flex-direction: column;
    align-items: center;
    color: var(--brand-red);
    font-weight: 700;
    text-align: center;
  }
  .brand__dot {
    width: 120px;
    height: 120px;
    border-radius: 50%;
    background: var(--brand-red);
    margin-bottom: 10px;
  }
  .brand__name {
    font-size: 40px;
    line-height: 44px;
    margin: 0;
    font-weight: 700;
  }
  .brand__tagline {
    font-size: 30px;
    line-height: 38px;
    margin: 0;
    font-weight: 700;
  }
  .card--front .brand {
    left: 103px;
    width: 300px;
    top: 156px;
  }
  .card--back .brand {
    left: 315px;
    width: 300px;
    top: 154px;
  }

  .contact {
    position: absolute;
    left: 537px;
    top: 78px;
    color: var(--text-white);
    font-size: 23px;
    line-height: 31px;
  }
  .contact p { margin: 0; white-space: nowrap; }
  .contact__name {
    color: var(--brand-red);
    font-size: 29px;
    font-weight: 700;
    line-height: 34px;
  }
  .contact__group { margin-top: 31px; }
  .contact__label { font-weight: 700; }
</style>
</head>
<body>
<main class="canvas">
  <section class="card card--front">
    <div class="brand">
      <span class="brand__dot" aria-hidden="true"></span>
      <p class="brand__name">Tails of Glee</p>
      <p class="brand__tagline">Pet Photography</p>
    </div>
    <div class="contact">
      <p class="contact__name">Declan Farrow</p>
      <p class="contact__role">Photographer</p>
      <div class="contact__group">
        <p>0497 560314</p>
        <p>declan@kwstudio.com.au</p>
        <p>www.tailsofglee.com.au</p>
      </div>
      <div class="contact__group">
        <p class="contact__label">Studio address</p>
        <p>27 Fennick Court, Elmvale 6112</p>
        <p class="contact__label">Postal Address</p>
        <p>8 Ormsby Ave,</p>
        <p>West Elmvale 6112</p>
      </div>
    </div>
  </section>

  <section class="card card--back">
    <div class="brand">
      <span class="brand__dot" aria-hidden="true"></span>
      <p class="brand__name">Tails of Glee</p>
      <p class="brand__tagline">Pet Photography</p>
    </div>
  </section>
</main>
</body>
</html>
```